Flyer for the Radiant Harvest Worship Day

I am looking to create a flyer for a one day prayer retreat our church is organizing.
This flyer will be posted on social media, websites and will also be printed so it can be mailed to people.
I am looking for something professional, with good use of our logo and band colors (logo colors).
I am counting on the designer's skill, creativity, art and knowledge of media communication to produce a flyer that will effectively and quickly convey the message we are trying to spread.
CONTENT OF THE FLYER:
Event title: Radiant Harvest Worship Day
Date: Tuesday July 2nd, 2019
Time: 11:00AM - 7:00PM
Bellmont Hotel, 4815 Alder Lane, Portland, Maine 04117 (Room: Willowmere)
Event Key words to highlight what the event is about: Prayer, Sharing the Word, Panel discussion, prophecy, Impartation.
Key phrases:
A one day prayer retreat.
Jesus Chris is Lord
Contact info:
www.tovelin.org
Phone: 207 555 0193
Email: contact@brookhavenfold.org

```html
<!DOCTYPE html>
<html lang="en">
<head>
<meta charset="utf-8">
<title>Radiant Harvest Worship Day</title>
<link rel="stylesheet" href="https://fonts.googleapis.com/css2?family=Montserrat:wght@400;600;800;900&family=Oswald:wght@500&family=Great+Vibes&family=Cinzel:wght@400;600&family=Crimson+Text:wght@400&display=swap">
<style>
  :root {
    --page: #ffffff;
    --ink: #17181e;
    --ink-deep: #101116;
    --orange: #f7951d;
    --white: #ffffff;
    --script: #8d8178;
    --navy: #1d2a44;
  }
  * { margin: 0; padding: 0; box-sizing: border-box; }
  html, body { width: 1200px; height: 1200px; overflow: hidden; background: var(--page); }
  .flyer {
    position: absolute; left: 237px; top: 86px; width: 725px; height: 1026px;
    background: radial-gradient(ellipse at 50% 40%, #25252b 0%, var(--ink) 55%, var(--ink-deep) 100%);
    overflow: hidden; color: var(--white);
  }
  .photo-hands {
    position: absolute; left: 0; top: 240px; width: 725px; height: 480px;
    background: radial-gradient(ellipse 42% 48% at 52% 38%, #cfc9c2 0%, #8e8880 35%, #3a3838 68%, rgba(23,24,30,0) 100%);
  }
  .title { position: absolute; left: 0; width: 100%; text-align: center; font-family: "Montserrat", sans-serif; font-weight: 900; line-height: 1; white-space: nowrap; }
  .title-top { top: 33px; font-size: 53px; color: var(--orange); letter-spacing: -0.5px; }
  .title-main { top: 80px; font-size: 70px; color: var(--white); letter-spacing: -1px; }
  .tagline { position: absolute; top: 164px; left: 0; width: 100%; text-align: center; font-family: "Montserrat", sans-serif; font-size: 15px; letter-spacing: 11px; font-weight: 400; padding-left: 11px; white-space: nowrap; }
  .script { position: absolute; top: 184px; left: 0; width: 100%; text-align: center; font-family: "Great Vibes", cursive; font-size: 50px; color: var(--script); white-space: nowrap; }
  .date { position: absolute; left: 111px; top: 604px; font-family: "Montserrat", sans-serif; font-weight: 900; font-size: 45px; line-height: 42px; letter-spacing: -0.5px; white-space: nowrap; }
  .year { position: absolute; left: 342px; top: 606px; width: 36px; height: 80px; background: var(--orange); color: var(--ink); font-family: "Montserrat", sans-serif; font-size: 24px; display: flex; align-items: center; justify-content: center; }
  .year span { transform: rotate(-90deg); display: block; letter-spacing: 1px; }
  .time { position: absolute; left: 389px; top: 600px; font-family: "Oswald", sans-serif; font-weight: 500; font-size: 38px; line-height: 44px; letter-spacing: -0.5px; white-space: nowrap; }
  .venue { position: absolute; left: 389px; top: 642px; font-family: "Montserrat", sans-serif; font-weight: 600; font-size: 13px; line-height: 15.5px; white-space: nowrap; }
  .highlights { position: absolute; left: 93px; top: 710px; width: 539px; height: 132px; border: 2px solid var(--white); border-radius: 10px; }
  .highlights .divider { position: absolute; left: 287px; top: 20px; width: 2px; height: 92px; background: linear-gradient(var(--orange), rgba(247,149,29,0.3)); }
  .highlights ul { position: absolute; list-style: none; font-family: "Cinzel", serif; font-size: 20px; }
  .highlights li { height: 30px; display: flex; align-items: center; gap: 10px; white-space: nowrap; }
  .highlights svg { width: 20px; height: 18px; }
  .col-left { left: 27px; top: 14px; }
  .col-right { left: 335px; top: 12px; }
  .brand { position: absolute; left: 48px; top: 918px; display: flex; align-items: center; gap: 6px; font-family: "Crimson Text", serif; font-size: 24px; line-height: 30px; white-space: nowrap; }
  .brand .dot { width: 10px; height: 10px; border-radius: 50%; background: var(--orange); }
  .rsvp { position: absolute; left: 202px; top: 893px; width: 228px; height: 32px; background: var(--orange); border-radius: 6px; color: var(--navy); font-family: "Crimson Text", serif; font-size: 29px; line-height: 32px; text-align: center; white-space: nowrap; }
  .phone { position: absolute; left: 446px; top: 881px; font-family: "Crimson Text", serif; font-size: 42px; line-height: 52px; white-space: nowrap; }
  .contact { position: absolute; top: 948px; display: flex; align-items: center; gap: 9px; font-family: "Crimson Text", serif; font-size: 14.5px; letter-spacing: 0.2px; white-space: nowrap; }
  .contact svg { width: 12px; height: 12px; }
  .contact-email { left: 205px; }
  .contact-web { left: 495px; }
</style>
</head>
<body>
<main class="flyer">
  <div class="photo-hands" role="img" aria-label="Photograph of clasped hands in prayer, softly lit against a dark background"></div>

  <h1>
    <span class="title title-top">RADIANT HARVEST</span>
    <span class="title title-main">WORSHIP DAY</span>
  </h1>
  <p class="tagline">A ONE DAY PRAYER RETREAT</p>
  <p class="script">Jesus Christ is Lord</p>

  <div class="date">TUESDAY<br>JULY 2ND</div>
  <div class="year"><span>2019</span></div>
  <div class="time">11:00AM-7:00PM</div>
  <p class="venue">Bellmont Hotel, 4815 Alder Lane,<br>Portland, Maine 04117<br>(Room: Willowmere)</p>

  <section class="highlights">
    <ul class="col-left">
      <li><svg viewBox="0 0 20 18"><path d="M2 9 L8 15 L18 2" fill="none" stroke="#f7951d" stroke-width="3"/></svg>Prayer</li>
      <li><svg viewBox="0 0 20 18"><path d="M2 9 L8 15 L18 2" fill="none" stroke="#f7951d" stroke-width="3"/></svg>Sharing the Word</li>
      <li><svg viewBox="0 0 20 18"><path d="M2 9 L8 15 L18 2" fill="none" stroke="#f7951d" stroke-width="3"/></svg>Panel discussion</li>
    </ul>
    <div class="divider"></div>
    <ul class="col-right">
      <li><svg viewBox="0 0 20 18"><path d="M2 9 L8 15 L18 2" fill="none" stroke="#f7951d" stroke-width="3"/></svg>PROPHECY</li>
      <li><svg viewBox="0 0 20 18"><path d="M2 9 L8 15 L18 2" fill="none" stroke="#f7951d" stroke-width="3"/></svg>Impartation</li>
    </ul>
  </section>

  <div class="brand"><span class="dot"></span><span>TOVELIN</span></div>
  <div class="rsvp">CALL TO RSVP</div>
  <div class="phone">207 555 0193</div>
  <div class="contact contact-email">
    <svg viewBox="0 0 13 13"><rect x="1" y="3" width="11" height="8" fill="#f7951d"/><path d="M1 3 L6.5 8 L12 3" fill="none" stroke="#17181e" stroke-width="1.2"/></svg>
    CONTACT@BROOKHAVENFOLD.ORG
  </div>
  <div class="contact contact-web">
    <svg viewBox="0 0 13 13"><circle cx="6.5" cy="6.5" r="5.5" fill="none" stroke="#f7951d" stroke-width="1.6"/><path d="M1 6.5 H12 M6.5 1 C3.5 4 3.5 9 6.5 12 M6.5 1 C9.5 4 9.5 9 6.5 12" fill="none" stroke="#f7951d" stroke-width="1"/></svg>
    WWW.TOVELIN.ORG
  </div>
</main>
</body>
</html>
```